Business card

We are looking for a creative person to deigns our company business card.

Target Market(s)

College age student

Industry/Entity Type

Accommodation

Contact Information for Business Card

We want a fun, clean and sophisticated design. It should look good, but more importantly the information should be legible.

Font styles to use
Serif
Sans Serif
Other font styles liked:
• Open Sans ,

Colors
33a6d7

Requirements
Must have
• Must have a young and memorable message. Be legible.
• Our logo on the back on a solid blue , please find color and logo attached
• LodgeBridgely.net on the back.
Nice to have
• I would like to have couple of different fonts on the LodgeBridgely.net on the back of the cards with a solid blue.

```html
<!DOCTYPE html>
<html lang="en">
<head>
<meta charset="utf-8">
<title>LodgeBridgely business card</title>
<link href="https://fonts.googleapis.com/css2?family=Lato:wght@400;700&family=Open+Sans:wght@700;800&display=swap" rel="stylesheet">
<style>
  :root {
    --brand-blue: #3b9bd6;
    --deep-blue: #0f4f86;
    --paper: #ffffff;
    --ink: #1c1c1c;
    --backdrop: #e9ebee;
  }
  * { margin: 0; padding: 0; box-sizing: border-box; }
  html, body { width: 1200px; height: 930px; overflow: hidden; }
  body { background: var(--backdrop); position: relative; font-family: "Lato", sans-serif; }

  .card {
    position: absolute;
    width: 700px; height: 400px;
    border-radius: 22px;
    overflow: hidden;
    box-shadow: 0 6px 18px rgba(0,0,0,.18);
  }

  /* back side */
  .card-back { left: 100px; top: 45px; background: var(--brand-blue); color: var(--paper); }
  .card-back .brand {
    position: absolute; left: 0; right: 0; top: 165px;
    text-align: center;
    font-family: "Open Sans", sans-serif; font-weight: 800;
    font-size: 50px; letter-spacing: -1px;
  }
  .card-back .brand-mark {
    display: block; width: 26px; height: 26px; margin: 0 auto 18px;
    background: var(--paper);
  }
  .card-back .site {
    position: absolute; left: 0; right: 0; top: 300px;
    text-align: center; font-size: 17px; letter-spacing: .3px;
  }

  /* front side */
  .card-front { left: 400px; top: 485px; background: var(--paper); }
  .card-front .swoosh { position: absolute; left: 0; top: 0; width: 700px; height: 400px; }
  .card-front .brand {
    position: absolute; left: 40px; top: 175px; width: 260px; text-align: center;
    font-family: "Open Sans", sans-serif; font-weight: 800;
    font-size: 32px; letter-spacing: -.8px; color: var(--deep-blue);
  }
  .card-front .divider {
    position: absolute; left: 325px; top: 80px; width: 2px; height: 190px;
    background: var(--deep-blue);
  }
  .details { position: absolute; left: 358px; top: 60px; color: var(--ink); }
  .details .name {
    font-family: "Open Sans", sans-serif; font-weight: 700;
    font-size: 27px; color: var(--deep-blue); letter-spacing: -.3px; line-height: 1.1;
  }
  .details .role { font-size: 17px; margin-bottom: 12px; }
  .details .address { font-size: 17px; line-height: 1.3; margin-bottom: 12px; }
  .contact-list { list-style: none; font-size: 17px; line-height: 1.35; }
  .contact-list li { display: flex; align-items: center; gap: 10px; }
  .contact-list svg { width: 14px; height: 14px; flex: none; }
</style>
</head>
<body>

<section class="card card-back" aria-label="Card back">
  <div class="brand"><span class="brand-mark"></span>LodgeBridgely</div>
  <div class="site">www.lodgebridgely.net</div>
</section>

<section class="card card-front" aria-label="Card front">
  <svg class="swoosh" viewBox="0 0 700 400" aria-hidden="true">
    <path d="M0,345 Q430,328 700,262 L700,400 L0,400 Z" fill="var(--brand-blue)"/>
    <path d="M200,330 Q470,305 700,250" fill="none" stroke="var(--deep-blue)" stroke-width="6"/>
  </svg>

  <div class="brand">LodgeBridgely</div>
  <div class="divider"></div>

  <div class="details">
    <div class="name">DANIEL MORENO</div>
    <div class="role">Director</div>
    <div class="address">718 Harlow St., Suite 302.<br>Denver, Colorado CO 80203</div>
    <ul class="contact-list">
      <li>
        <svg viewBox="0 0 24 24"><path fill="var(--deep-blue)" d="M6.6 10.8a15 15 0 0 0 6.6 6.6l2.2-2.2a1 1 0 0 1 1-.25 11 11 0 0 0 3.6.6 1 1 0 0 1 1 1V20a1 1 0 0 1-1 1A17 17 0 0 1 3 4a1 1 0 0 1 1-1h3.5a1 1 0 0 1 1 1c0 1.25.2 2.45.6 3.6a1 1 0 0 1-.25 1z"/></svg>
        +330 5172-4039
      </li>
      <li>
        <svg viewBox="0 0 24 24"><rect x="3" y="5" width="18" height="14" rx="1" fill="none" stroke="var(--deep-blue)" stroke-width="2"/><path d="M3 6l9 7 9-7" fill="none" stroke="var(--deep-blue)" stroke-width="2"/></svg>
        info@lodgebridgely.net
      </li>
      <li>
        <svg viewBox="0 0 24 24"><circle cx="12" cy="12" r="9" fill="none" stroke="var(--deep-blue)" stroke-width="2"/><path d="M3 12h18M12 3c3 3 3 15 0 18M12 3c-3 3-3 15 0 18" fill="none" stroke="var(--deep-blue)" stroke-width="1.6"/></svg>
        www.lodgebridgely.net
      </li>
    </ul>
  </div>
</section>

</body>
</html>
```